Health and Wellness. I am an energetic, but not over the top, Certified Personal Trainer and Nutriti

I need a flyer, 8.5 x 11, representing my company to be displayed in a Doctor's office that specializes in Pain Medicine. Most, if not all, of these clients experience pain or have some chronic diseases such as high blood pressure, high cholesterol, back pain, joint pain, etc. So the flyer should convey that exercise and nutrition reduce/relieves pain and references some of these ailments. Ideally, the flyer should depict an overweight person exercising with a content, or somewhat content or smiling expression on their face in some part of the flyer. My services cover nutrition and include personal training to where I Ideally train people in their home, equipment permitting, or outside in our local Floridian Parks, and sometimes beaches. This flyer will be in a display case, and the bottom right 8.5 x5 cm will need to be blank, or allow for me to input the back of my business car into it, as I'll have business cards readily available in front of the flyer to be taken. I've included some versions of my logos to be added to the flyer. The other picture is of the flyer holder, with business card area, that this flyer will be presented in. Finally, I've attached a pic of what the back of my business card looks like to be input into that bottom right hand corner. You'll be able to see the area in the bottom right that will display my business cards.
Target Market(s)
People looking for weight loss through Nutrition and Fitness. Those looking to relieve joint and/or back pain or those with Chronic diseases such as high blood pressure, high cholesterol, etc.
Industry/Entity Type
Doctor
Requirements
Must have
- Resemble my Logo's color scheme: Red, Teal, and Grey. Some type of photo of an overweight or slightly overweight person exercising.

```html
<!DOCTYPE html>
<html lang="en">
<head>
<meta charset="utf-8">
<title>Brightwell Fitness Flyer</title>
<link href="https://fonts.googleapis.com/css2?family=Montserrat:wght@400;500;700;800&display=swap" rel="stylesheet">
<style>
  :root {
    --brand-red: #c41e45;
    --brand-red-dark: #9e1533;
    --ink-grey: #5a5a5a;
    --ink-dark: #2e2e2e;
    --band-grey: #6b6b6b;
    --paper: #f4f4f4;
    --white: #ffffff;
  }
  * { margin: 0; padding: 0; box-sizing: border-box; }
  html, body { width: 930px; height: 1200px; overflow: hidden; background: var(--paper); }
  .flyer { position: relative; width: 930px; height: 1200px; overflow: hidden; font-family: "Montserrat", sans-serif; }
  .flyer-shapes { position: absolute; inset: 0; }
  .brand { position: absolute; left: 34px; top: 64px; width: 250px; text-align: center; }
  .brand-mark { width: 78px; height: 78px; margin: 0 auto 14px; border: 6px solid var(--brand-red); border-radius: 50%; }
  .brand-name { font-weight: 700; font-size: 27px; line-height: 30px; letter-spacing: 2px; color: var(--ink-grey); }
  .headline { position: absolute; left: 37px; top: 540px; font-weight: 800; font-size: 39px; line-height: 44px; color: var(--ink-grey); text-transform: uppercase; letter-spacing: 0.5px; }
  .headline .accent { color: var(--brand-red); }
  .intro { position: absolute; left: 36px; top: 774px; width: 551px; font-size: 14px; line-height: 18.5px; color: var(--ink-dark); text-align: justify; }
  .intro p + p { margin-top: 5px; }
  .services-tab { position: absolute; left: 0; top: 912px; width: 62px; height: 120px; background: var(--brand-red); border-radius: 0 0 0 24px; display: flex; align-items: center; justify-content: center; }
  .services-tab span { transform: rotate(-90deg); color: var(--white); font-weight: 800; font-size: 17px; letter-spacing: 1px; white-space: nowrap; }
  .service { position: absolute; top: 922px; width: 180px; margin-left: -90px; text-align: center; }
  .service svg { display: block; margin: 0 auto 8px; }
  .service-label { font-weight: 700; font-size: 18px; line-height: 24px; color: var(--ink-grey); text-transform: uppercase; }
  .social-bars { position: absolute; left: 0; top: 1058px; width: 60px; }
  .social-bar { height: 24px; margin-bottom: 4px; background: var(--brand-red); border-radius: 0 0 0 12px; display: flex; align-items: center; justify-content: flex-end; padding-right: 4px; }
  .social-bar:nth-child(2) { background: var(--brand-red-dark); }
  .social-bar:nth-child(4) { background: var(--brand-red-dark); }
  .social-dot { width: 19px; height: 19px; border-radius: 50%; border: 2px solid var(--white); }
  .contact { position: absolute; left: 84px; top: 1054px; }
  .contact-title { font-weight: 500; font-size: 19px; color: var(--ink-grey); }
  .contact-title strong { color: var(--brand-red); font-weight: 700; }
  .contact-rule { width: 42px; height: 2px; background: var(--brand-red); margin: 6px 0 10px; }
  .contact-line { display: flex; align-items: center; gap: 10px; font-size: 18px; line-height: 24.5px; color: var(--ink-grey); }
  .contact-line svg { flex: none; }
</style>
</head>
<body>
<div class="flyer">
  <svg class="flyer-shapes" width="930" height="1200" viewBox="0 0 930 1200">
    <defs>
      <linearGradient id="gymTone" x1="0" y1="0" x2="1" y2="1">
        <stop offset="0" stop-color="#8a7e78"/>
        <stop offset="0.45" stop-color="#d9a68a"/>
        <stop offset="0.75" stop-color="#e0583f"/>
        <stop offset="1" stop-color="#b9b4b0"/>
      </linearGradient>
      <radialGradient id="parkTone" cx="0.5" cy="0.4" r="0.7">
        <stop offset="0" stop-color="#7f8c6a"/>
        <stop offset="0.6" stop-color="#5e6b52"/>
        <stop offset="1" stop-color="#8a8580"/>
      </radialGradient>
      <linearGradient id="bandGrey" x1="0" y1="0" x2="1" y2="0">
        <stop offset="0" stop-color="#4c4c4c"/>
        <stop offset="0.6" stop-color="#8a8a8a"/>
        <stop offset="1" stop-color="#d8d8d8"/>
      </linearGradient>
    </defs>

    <rect x="0" y="0" width="930" height="640" fill="url(#gymTone)" role="img" aria-label="Photo of a smiling woman in a red shirt exercising on an elliptical machine in a gym"/>

    <path d="M0,0 H350 C392,40 392,150 330,210 C280,255 160,250 90,275 C40,292 14,315 0,335 Z" fill="#5c5c5c"/>
    <path d="M0,0 H338 C378,42 376,146 318,200 C268,244 150,240 82,262 C36,278 12,300 0,318 Z" fill="var(--paper)"/>

    <path d="M600,640 C700,650 760,640 930,600 V1200 H600 Z" fill="var(--brand-red)"/>

    <path d="M0,515 C160,480 380,490 560,540 C700,580 820,580 930,520 V600 C820,650 700,650 560,610 C380,560 160,550 0,600 Z" fill="url(#bandGrey)"/>
    <path d="M0,560 C160,525 380,535 540,580 C640,610 700,650 730,700 C770,780 790,880 776,1000 C770,1080 750,1150 725,1200 H0 Z" fill="#707070"/>
    <path d="M0,572 C160,540 380,550 530,594 C625,624 682,660 712,710 C750,790 768,885 756,1000 C750,1080 730,1150 705,1200 H0 Z" fill="var(--paper)"/>

    <circle cx="738" cy="714" r="160" fill="var(--white)"/>
    <circle cx="738" cy="714" r="148" fill="url(#parkTone)" role="img" aria-label="Photo of two women doing push-ups together in a park"/>
  </svg>

  <div class="brand">
    <div class="brand-mark"></div>
    <div class="brand-name">BRIGHTWELL<br>FITNESS</div>
  </div>

  <h1 class="headline">Helping<br>you to <span class="accent">lose</span><br><span class="accent">weight, gain</span><br><span class="accent">muscle</span>, and own<br>the room</h1>

  <div class="intro">
    <p>Millions of Americans are out of shape and don't know where to start. My name is Marcus, owner of Brightwell Fitness, I can show you where to begin.</p>
    <p>My services cover nutrition and include personal training to where I Ideally train people in their home, equipment permitting, or outside in our local Floridian Parks, and sometimes beaches.</p>
  </div>

  <div class="services-tab"><span>SERVICES</span></div>

  <div class="service" style="left:125px">
    <svg width="40" height="44" viewBox="0 0 40 44" fill="none" stroke="var(--brand-red)" stroke-width="2" stroke-linecap="round" stroke-linejoin="round"><path d="M16 26 V8 a3 3 0 0 1 6 0 V22 M22 20 a3 3 0 0 1 6 0 V24 M28 22 a3 3 0 0 1 6 0 V32 c0 6 -4 10 -10 10 h-4 c-4 0 -7 -3 -9 -6 L6 28 a3 3 0 0 1 5 -3 l5 5"/><path d="M11 9 a8 8 0 0 1 16 0"/></svg>
    <div class="service-label">Online<br>Fitness</div>
  </div>
  <div class="service" style="left:255px">
    <svg width="44" height="44" viewBox="0 0 44 44" fill="none" stroke="var(--brand-red)" stroke-width="2" stroke-linejoin="round"><path d="M4 22 L22 5 L40 22 M9 18 V40 H35 V18"/><rect x="18" y="28" width="8" height="12"/></svg>
    <div class="service-label">Your Home<br>Fitness</div>
  </div>
  <div class="service" style="left:429px">
    <svg width="48" height="44" viewBox="0 0 48 44" fill="none" stroke="var(--brand-red)" stroke-width="2" stroke-linecap="round"><circle cx="34" cy="12" r="5"/><path d="M34 2v3 M34 19v3 M24 12h3 M41 12h3 M27 5l2 2 M39 17l2 2 M41 5l-2 2"/><path d="M4 6 l4 3 l4 -3 M4 13 l4 3 l4 -3"/><path d="M4 26 q5 -4 10 0 t10 0 t10 0 t10 0 M4 33 q5 -4 10 0 t10 0 t10 0 t10 0 M4 40 q5 -4 10 0 t10 0 t10 0 t10 0"/></svg>
    <div class="service-label">Park &amp; Beaches<br>Fitness</div>
  </div>
  <div class="service" style="left:626px">
    <svg width="64" height="48" viewBox="0 0 64 48" fill="none" stroke="var(--brand-red)" stroke-width="2" stroke-linejoin="round"><path d="M6 44 L24 14 L38 30 Z"/><path d="M12 36 L30 22 M17 40 L34 27"/><circle cx="44" cy="8" r="3"/><circle cx="54" cy="16" r="2.5"/><path d="M40 20 l3 -3 M48 26 l4 0 M36 6 l0 -4"/></svg>
    <div class="service-label">Bridal Party<br>Fitness</div>
  </div>

  <div class="social-bars">
    <div class="social-bar"><div class="social-dot"></div></div>
    <div class="social-bar"><div class="social-dot"></div></div>
    <div class="social-bar"><div class="social-dot"></div></div>
    <div class="social-bar"><div class="social-dot"></div></div>
  </div>

  <div class="contact">
    <div class="contact-title">Contact <strong>Us</strong> :</div>
    <div class="contact-rule"></div>
    <div class="contact-line">
      <svg width="17" height="17" viewBox="0 0 20 20"><circle cx="10" cy="10" r="10" fill="var(--brand-red)"/><path d="M6.5 5 l2 0 l1 3 l-1.3 1 c0.8 1.5 1.8 2.5 3.3 3.3 l1 -1.3 l3 1 l0 2 c-5 0.5 -9.5 -4 -9 -9 z" fill="var(--white)"/></svg>
      <span>555-014-2283</span>
    </div>
    <div class="contact-line">
      <svg width="17" height="17" viewBox="0 0 20 20"><circle cx="10" cy="10" r="10" fill="var(--brand-red)"/><rect x="5" y="6.5" width="10" height="7" fill="none" stroke="var(--white)" stroke-width="1.4"/><path d="M5 6.5 l5 4 l5 -4" fill="none" stroke="var(--white)" stroke-width="1.4"/></svg>
      <span>hello@brightwellfitness.com</span>
    </div>
    <div class="contact-line">
      <svg width="17" height="17" viewBox="0 0 20 20"><circle cx="10" cy="10" r="10" fill="var(--brand-red)"/><g fill="none" stroke="var(--white)" stroke-width="1.2"><circle cx="10" cy="10" r="5.5"/><ellipse cx="10" cy="10" rx="2.3" ry="5.5"/><path d="M4.5 10 h11"/></g></svg>
      <span>www.brightwellfitness.com</span>
    </div>
  </div>
</div>
</body>
</html>
```